Volunteer Fire Department Website Refresh

I need a redesign of a website, www.plbrigade.org, I built for a volunteer fire department several years ago. I plan to reuse the existing content except for the stock photos on the landing page. I would like the website to be responsive and mobile friendly, using bootstrap 4 and the use of Material Design is optional. Overall I would like to stick with a darker color scheme with dark gray, red, and yellow similar to this template https://www.layoutgrove.com/demo/51937.html
Industry/Entity Type
Fire Department
Coding
Coded - Design and coding required
Number of Pages Required
5+ page
Look and feel
Each slider illustrates characteristics of the customer's brand and the style your logo design should communicate.

```html
<!DOCTYPE html>
<html lang="en">
<head>
<meta charset="utf-8">
<title>Pine Lake Volunteer Fire Department</title>
<link href="https://fonts.googleapis.com/css2?family=Oswald:wght@400;500;600&family=Open+Sans:ital,wght@0,400;0,600;0,700;1,400&display=swap" rel="stylesheet">
<style>
:root{
  --dark:#1c1c1e;
  --panel:#2e2e30;
  --red:#a3182b;
  --red-deep:#7e0f1f;
  --yellow:#f2a51f;
  --light:#f0f0f0;
  --grey-band:#e4e4e4;
  --text:#555;
  --white:#fff;
}
*{box-sizing:border-box;margin:0;padding:0}
html,body{width:1200px;height:2224px;overflow:hidden}
body{font-family:"Open Sans",Arial,sans-serif;color:var(--text);background:var(--light);position:relative}
a{color:inherit;text-decoration:none}
.site-header{position:absolute;left:0;top:0;width:1200px;height:100px;background:var(--dark);z-index:2}
.brand{position:absolute;left:60px;top:28px;display:flex;align-items:center;gap:10px;font-family:"Oswald",sans-serif;font-weight:500;font-size:24px;color:var(--white)}
.brand-mark{width:20px;height:20px;background:var(--red);border-radius:50%}
.top-contact{position:absolute;right:40px;top:10px;display:flex;gap:22px;font-size:12px;color:#ccc}
.top-contact span{display:flex;align-items:center;gap:6px}
.main-nav{position:absolute;right:40px;top:52px;display:flex;gap:30px;font-size:15px;color:var(--white)}
.main-nav .active{color:var(--yellow)}
.hero{position:absolute;left:0;top:100px;width:1200px;height:500px;background:linear-gradient(160deg,#3b2a24 0%,#8a3a1c 45%,#c55a1f 60%,#4a3a34 100%)}
.hero-caption{position:absolute;left:0;top:165px;width:1200px;text-align:center;color:var(--white)}
.hero-title{font-family:"Oswald",sans-serif;font-weight:600;font-size:74px;letter-spacing:2px;line-height:1}
.hero-sub{font-family:"Oswald",sans-serif;font-size:32px;margin-top:6px}
.hero-arrow{position:absolute;top:240px;color:rgba(255,255,255,.7);font-size:30px}
.welcome{position:absolute;left:0;top:600px;width:1200px;height:340px;display:flex}
.welcome-text{width:730px;background:var(--red);color:var(--white);padding:44px 60px 0 100px}
.welcome-text h2{font-family:"Oswald",sans-serif;font-weight:500;font-size:30px;margin-bottom:14px}
.welcome-text p{font-size:14px;line-height:1.6}
.btn{display:inline-block;background:var(--yellow);color:var(--white);font-size:13px;padding:7px 20px;border-radius:3px;margin-top:26px}
.welcome-photo{flex:1;background:linear-gradient(135deg,#c9d7e3 0%,#b8202c 50%,#6c1a1f 100%)}
.ranking{position:absolute;left:88px;top:1032px;width:340px;height:568px;background:var(--panel)}
.ranking h3{background:var(--yellow);color:var(--white);font-family:"Oswald",sans-serif;font-weight:500;font-size:24px;height:58px;line-height:58px;text-align:center}
.member{display:flex;align-items:center;height:100px;padding-left:34px;gap:22px;color:var(--white)}
.avatar{width:62px;height:62px;border-radius:50%;background:#8a7b70;border:3px solid #555}
.member-name{font-family:"Oswald",sans-serif;font-size:20px}
.member-stat{font-size:13px;color:#ccc;margin-top:2px}
.member-stat b{color:var(--white);margin-left:10px}
.what-we-do{position:absolute;left:470px;top:1050px;width:640px}
.section-title{font-family:"Oswald",sans-serif;font-weight:500;font-size:28px;color:#222}
.what-we-do p{font-size:14px;line-height:1.6;margin-top:10px}
.read-more{color:var(--yellow);font-size:13px;display:inline-block;margin-top:10px}
.events{position:absolute;left:470px;top:1280px;width:640px}
.events-arrows{position:absolute;right:0;top:4px;color:var(--yellow);font-size:22px;letter-spacing:8px}
.event-cards{display:flex;gap:30px;margin-top:18px}
.event-card{width:300px;height:300px;background:var(--white);text-align:center}
.event-photo{height:120px;background:linear-gradient(180deg,#6f8fb0,#6b5a56)}
.event-card h4{font-family:"Oswald",sans-serif;font-weight:500;font-size:16px;color:#333;margin:16px 0 8px}
.event-card p{font-size:13px;line-height:1.55;padding:0 28px}
.partners{position:absolute;left:0;top:1700px;width:1200px;height:180px;background:var(--grey-band);display:flex;justify-content:center;align-items:center;gap:40px}
.partner{width:160px;height:100px;background:var(--white);border-radius:4px;box-shadow:0 1px 4px rgba(0,0,0,.15);display:flex;align-items:center;justify-content:center}
.partner i{width:90px;height:22px;background:#c8c8c8;border-radius:3px;display:block}
.site-footer{position:absolute;left:0;top:1880px;width:1200px;height:344px;background:var(--dark);color:#bbb}
.footer-col{position:absolute;top:50px;font-size:13px;line-height:1.9}
.footer-col h5{font-family:"Oswald",sans-serif;font-weight:500;font-size:16px;color:var(--white);margin-bottom:10px}
.footer-col li{list-style:none}
.footer-col li::before{content:"› ";color:var(--yellow)}
.subscribe{display:flex;margin-top:12px}
.subscribe span{width:170px;height:30px;background:var(--white);color:#999;font-size:12px;padding:5px 8px}
.subscribe b{width:60px;height:30px;background:var(--yellow);color:var(--white);font-size:12px;text-align:center;line-height:30px;font-weight:400}
.social{display:flex;gap:10px;margin-top:4px}
.social i{width:28px;height:28px;background:#555;border-radius:3px;display:block}
.copyright{position:absolute;left:0;bottom:0;width:1200px;height:70px;line-height:70px;text-align:center;font-size:12px;color:#999;border-top:1px solid #333}
</style>
</head>
<body>
<header class="site-header">
  <div class="brand"><span class="brand-mark"></span>Pine Lake VFD</div>
  <div class="top-contact">
    <span><svg width="12" height="12" viewBox="0 0 24 24"><path fill="#f2a51f" d="M6.6 10.8a15 15 0 006.6 6.6l2.2-2.2c.3-.3.7-.4 1-.2 1.1.4 2.3.6 3.6.6.6 0 1 .4 1 1V20c0 .6-.4 1-1 1A17 17 0 013 4c0-.6.4-1 1-1h3.5c.6 0 1 .4 1 1 0 1.2.2 2.4.6 3.6.1.3 0 .7-.2 1z"/></svg>1-555-204-7781</span>
    <span><svg width="13" height="10" viewBox="0 0 26 20"><rect x="1" y="1" width="24" height="18" fill="none" stroke="#f2a51f" stroke-width="2"/><path d="M1 1l12 10L25 1" fill="none" stroke="#f2a51f" stroke-width="2"/></svg>info@plbrigade.org</span>
  </div>
  <nav class="main-nav">
    <a class="active">Home</a><a>History</a><a>Equipment</a><a>Members</a><a>Gallery</a><a>Alarms</a><a>Training</a><a>Join now</a>
  </nav>
</header>

<section class="hero" role="img" aria-label="Firefighters spraying water hoses at a burning building">
  <span class="hero-arrow" style="left:30px">‹</span>
  <div class="hero-caption">
    <h1 class="hero-title">PINE LAKE</h1>
    <p class="hero-sub">Porro quisquam est qui dolorem</p>
  </div>
  <span class="hero-arrow" style="right:30px">›</span>
</section>

<section class="welcome">
  <div class="welcome-text">
    <h2>WELCOME TO PINE LAKE</h2>
    <p>It is a long established fact that a reader will be distracted by the readable content of a page when looking at its layout. The point of using Lorem Ipsum is that it has a more-or-less normal distribution of letters, as opposed to using 'Content here, content here', making it look like readable English. Many desktop publishing packages and web page editors now use Lorem Ipsum as their default model text, and a search for 'lorem ipsum' will uncover.</p>
    <a class="btn">Read more</a>
  </div>
  <div class="welcome-photo" role="img" aria-label="Red fire engine parked with a firefighter beside it"></div>
</section>

<aside class="ranking">
  <h3>TOP FIREFIGHTERS 2018</h3>
  <div class="member"><span class="avatar" role="img" aria-label="Portrait of Carl Mercer"></span><div><div class="member-name">CARL MERCER</div><div class="member-stat">Attendance : 26 <b>96%</b></div></div></div>
  <div class="member"><span class="avatar" role="img" aria-label="Portrait of Grant Dawson"></span><div><div class="member-name">GRANT DAWSON</div><div class="member-stat">Attendance : 20 <b>74%</b></div></div></div>
  <div class="member"><span class="avatar" role="img" aria-label="Portrait of Ruben Galvez"></span><div><div class="member-name">RUBEN GALVEZ</div><div class="member-stat">Attendance : 19 <b>70%</b></div></div></div>
  <div class="member"><span class="avatar" role="img" aria-label="Portrait of Jason Moreau"></span><div><div class="member-name">JASON MOREAU</div><div class="member-stat">Attendance : 18 <b>67%</b></div></div></div>
  <div class="member"><span class="avatar" role="img" aria-label="Portrait of Dean Dorsey"></span><div><div class="member-name">DEAN DORSEY</div><div class="member-stat">Attendance : 11 <b>44%</b></div></div></div>
</aside>

<section class="what-we-do">
  <h2 class="section-title">WHAT WE DO</h2>
  <p>It is a long established fact that a reader will be distracted by the readable content of a page when looking at its layout. The point of using Lorem Ipsum is that it has a more-or-less normal distribution of letters, as opposed to using 'Content here, content here', making it look like readable English. Many desktop publishing packages and web page editors now use Lorem Ipsum as their default model text, and a search for 'lorem ipsum' will uncover.</p>
  <a class="read-more">Read More »</a>
</section>

<section class="events">
  <h2 class="section-title">UPCOMING EVENTS</h2>
  <span class="events-arrows">‹›</span>
  <div class="event-cards">
    <article class="event-card">
      <div class="event-photo" role="img" aria-label="Volunteer crew gathered in front of the station"></div>
      <h4>PORRO QUISQUAM</h4>
      <p>It is a long established fact that a reader will be drawn by the readable content.</p>
      <a class="read-more">Read More »</a>
    </article>
    <article class="event-card">
      <div class="event-photo" role="img" aria-label="Firefighters training beside an engine"></div>
      <h4>PORRO QUISQUAM</h4>
      <p>It is a long established fact that a reader will be drawn by the readable content.</p>
      <a class="read-more">Read More »</a>
    </article>
  </div>
</section>

<section class="partners" aria-label="Partners">
  <div class="partner"><i></i></div>
  <div class="partner"><i></i></div>
  <div class="partner"><i></i></div>
  <div class="partner"><i></i></div>
  <div class="partner"><i></i></div>
</section>

<footer class="site-footer">
  <div class="footer-col" style="left:88px">
    <h5>INFORMATION</h5>
    <ul><li>Privacy Policy</li><li>Plan Ahead</li><li>Advanced Search</li><li>Contact Us</li></ul>
  </div>
  <div class="footer-col" style="left:360px">
    <h5>CONTACT US</h5>
    <div>2210 Ridge Ave, Pine Lake, TX</div>
    <div>1-555-204-7781</div>
    <div>info@plbrigade.org</div>
  </div>
  <div class="footer-col" style="left:640px">
    <h5>JOIN OUR MAILING LIST</h5>
    <div>Get news and alerts sent to your inbox.</div>
    <div class="subscribe"><span>Enter address</span><b>Join</b></div>
  </div>
  <div class="footer-col" style="left:940px">
    <h5>FOLLOW US OUT THERE</h5>
    <div class="social"><i></i><i></i><i></i><i></i><i></i></div>
  </div>
  <div class="copyright">Copyright © 2018 All Rights Reserved</div>
</footer>
</body>
</html>
```